Business Card design

Keen on a very modern design with using the red star as a feature point preferably will have it printed with red foiling.

Target Market(s)

Cosmetics

Industry/Entity Type

Cosmetics

Contact Information for Business Card

Marcie Budd
Director
9 Frey Avenue
Doveton West Victoria
Australia 3618
marcie@glowpactsupply.com.au

Font styles to use
Sans Serif

Colors
ec1f27
000000

Requirements
Must have
• Keen on some red stars on back with black background and I may get the red components printed as red foiling potentially

```html
<!DOCTYPE html>
<html lang="en">
<head>
<meta charset="utf-8">
<title>Glowpact Business Card</title>
<link rel="stylesheet" href="https://fonts.googleapis.com/css2?family=Roboto:wght@400;700;900&display=swap">
<style>
  :root {
    --brand-red: #ec1f27;
    --foil-red: #c4161d;
    --ink: #000000;
    --text: #1c1c1c;
    --card: #f1efec;
    --backdrop: #d9d3ca;
  }
  * { margin: 0; padding: 0; box-sizing: border-box; }
  html, body {
    width: 1200px;
    height: 970px;
    overflow: hidden;
    background: var(--backdrop);
    font-family: "Roboto", Arial, sans-serif;
  }
  .card {
    position: absolute;
    left: 80px;
    top: 190px;
    width: 1040px;
    height: 590px;
    background: var(--card);
    border-radius: 26px;
    overflow: hidden;
    box-shadow: 0 10px 30px rgba(0, 0, 0, 0.18);
  }
  .card__ornament {
    position: absolute;
    left: 680px;
    top: 0;
    width: 360px;
    height: 590px;
    background:
      radial-gradient(ellipse 45% 30% at 70% 78%, rgba(196, 22, 29, 0.55), rgba(196, 22, 29, 0) 100%),
      radial-gradient(ellipse 40% 28% at 45% 40%, rgba(196, 22, 29, 0.35), rgba(196, 22, 29, 0) 100%),
      linear-gradient(160deg, rgba(0, 0, 0, 0.10) 0%, rgba(0, 0, 0, 0.04) 60%, rgba(0, 0, 0, 0) 100%);
  }
  .brand-name {
    position: absolute;
    left: 48px;
    top: 58px;
    font-weight: 900;
    font-size: 118px;
    letter-spacing: -3px;
    line-height: 1;
    color: var(--ink);
  }
  .contact {
    position: absolute;
    left: 46px;
    top: 304px;
    color: var(--text);
  }
  .contact__name {
    font-weight: 700;
    font-size: 34px;
    letter-spacing: 0.5px;
    line-height: 1.1;
  }
  .contact__role {
    font-size: 26px;
    color: var(--brand-red);
    margin-top: 4px;
  }
  .contact__address {
    font-size: 26px;
    line-height: 33px;
    margin-top: 38px;
    font-style: normal;
  }
  .contact__email {
    display: flex;
    align-items: center;
    gap: 10px;
    font-size: 26px;
    margin-top: 10px;
    margin-left: -3px;
  }
  .contact__email svg { flex: none; }
</style>
</head>
<body>
  <section class="card" aria-label="Glowpact business card">
    <div class="card__ornament" role="img" aria-label="Decorative swirl of black lines with red foil stars"></div>

    <div class="brand-name">Glowpact</div>

    <div class="contact">
      <div class="contact__name">Marcie Budd</div>
      <div class="contact__role">Director</div>
      <address class="contact__address">
        9 Frey Avenue<br>
        Doveton West Victoria<br>
        Australia 3618
      </address>
      <div class="contact__email">
        <svg width="30" height="30" viewBox="0 0 30 30" aria-hidden="true">
          <circle cx="15" cy="15" r="13" fill="none" stroke="var(--brand-red)" stroke-width="2"/>
          <rect x="8" y="10" width="14" height="10" fill="var(--brand-red)"/>
          <path d="M8 10 L15 16 L22 10" fill="none" stroke="var(--card)" stroke-width="1.5"/>
        </svg>
        <span>marcie@glowpactsupply.com.au</span>
      </div>
    </div>
  </section>
</body>
</html>
```